Business Card Design Project

Hello- I am an interior stylist/product designer whose work is detail driven, very clean and transitional in style and I want my business card to reflect those qualities. I have a logo that I use on my website- my name and a hand drawn chandelier that I want incorporated into the design. However, "Design for the Home" needs to be changed to "Designs". I will be using cream colored stock and am thinking of gray text and logo. I need your help in pulling my card together since it will be the most used element and drive the design of the rest of my stationary suite.
Updates

Please note that I have changed my QR code from my cell # to my website. The new code will be downloaded now.

Reason: I want to thank everyone who has submitted designs- there are truly some very inspiring designs and I am very pleased. I want to make certain that I get this right and have an attractive and highly effective marketing tool when we are finished. With that said, I have run into a technical problem with one aspect of the card- a qr code for my website that was not part of the original brief. I will get that corrected today and post. Once I get that taken care of, I will post comments to all designs received do far. Thanks again for everyone's efforts, Mari

QR Code for the website is now uploaded. Thanks for your patience!

Target Market(s)

Upper middle class- mostly women

Industry/Entity Type

Business

Requirements
Must have
• Maribel Foster Designs
"...in every single room."
214-555-0186
maribelfoster@velmorix.net
www.maribelfosterdesigns-studio.com
10873 Willowmere Lane
Brenmoor, TX 75418
Nice to have
• Mari Foster
Owner

```html
<!DOCTYPE html>
<html lang="en">
<head>
<meta charset="utf-8">
<title>Maribel Foster Designs – Business Card</title>
<link rel="stylesheet" href="https://fonts.googleapis.com/css2?family=Arimo:ital@0;1&family=Cormorant+Garamond:ital,wght@0,500;1,500&display=swap">
<style>
  :root {
    --card-bg: #ffffff;
    --pattern-light: #eef0f0;
    --pattern-mid: #c9cecf;
    --divider: #5b6566;
    --ink-dark: #4a5556;
    --ink-mid: #5f6a6b;
    --ink-soft: #939b9b;
  }
  html, body {
    margin: 0;
    padding: 0;
    width: 1200px;
    height: 750px;
    overflow: hidden;
    background: var(--card-bg);
  }
  .card {
    position: relative;
    width: 1200px;
    height: 750px;
    background: var(--card-bg);
    font-family: "Arimo", Arial, sans-serif;
    color: var(--ink-dark);
  }
  .pattern-panel {
    position: absolute;
    left: 0;
    top: 0;
    width: 419px;
    height: 750px;
    background: linear-gradient(180deg, var(--pattern-mid) 0%, #d3d7d8 55%, var(--pattern-light) 100%);
  }
  .divider {
    position: absolute;
    left: 419px;
    top: 0;
    width: 19px;
    height: 750px;
    background: var(--divider);
  }
  .brand {
    position: absolute;
    left: 700px;
    top: 156px;
    width: 434px;
    text-align: center;
  }
  .brand-name {
    margin: 0;
    font-family: "Cormorant Garamond", Georgia, serif;
    font-weight: 500;
    font-size: 52px;
    line-height: 62px;
    color: var(--ink-mid);
  }
  .brand-sub {
    margin: 12px 0 0;
    font-size: 19px;
    line-height: 22px;
    color: var(--ink-soft);
  }
  .tagline {
    margin: 13px 0 0;
    font-family: "Cormorant Garamond", Georgia, serif;
    font-style: italic;
    font-size: 21px;
    line-height: 24px;
    color: var(--ink-dark);
  }
  .contact {
    position: absolute;
    left: 478px;
    top: 293px;
  }
  .person-name {
    margin: 0;
    font-size: 38px;
    line-height: 46px;
    font-weight: 400;
    color: var(--ink-dark);
  }
  .person-role {
    margin: 0;
    font-style: italic;
    font-size: 27px;
    line-height: 30px;
    color: var(--ink-dark);
  }
  .details {
    margin: 32px 0 0;
    font-size: 30px;
    line-height: 43px;
    color: var(--ink-dark);
  }
  .online {
    margin: 20px 0 0;
    font-size: 30px;
    line-height: 42px;
    color: var(--ink-dark);
  }
  .details p, .online p { margin: 0; }
</style>
</head>
<body>
  <main class="card">
    <div class="pattern-panel" role="img" aria-label="Soft grey damask pattern fading toward the bottom"></div>
    <div class="divider"></div>

    <header class="brand">
      <p class="brand-name">Maribel Foster</p>
      <p class="brand-sub">Designs</p>
      <p class="tagline">“...in every single room.”</p>
    </header>

    <section class="contact">
      <h1 class="person-name">Mari Foster</h1>
      <p class="person-role">owner</p>
      <div class="details">
        <p>214-555-0186</p>
        <p>10873 Willowmere Lane</p>
        <p>Brenmoor, TX 75418</p>
      </div>
      <div class="online">
        <p>maribelfoster@velmorix.net</p>
        <p>www.maribelfosterdesigns-studio.com</p>
      </div>
    </section>
  </main>
</body>
</html>
```